Book cover design for the book titled "Quieter Under Lanterns."

create a book cover. The book title is, "Quieter Under Lanterns: A Ledger of Harbour Songs Across Mild Winters." The purpose of the book is to create awareness of how childhood trauma is impacting 7 out of 10 adults in the world today and that two-thirds of children will experience neglect and or abuse before their 18th birthday. One victim described that his mental and physical illness resulting from childhood trauma felt like he wa being pulled to the ground, that the force was "quieter under lanterns." The design should be clean and simple and communicate a crisis.

```html
<!DOCTYPE html>
<html lang="en">
<head>
<meta charset="utf-8">
<title>Quieter Under Lanterns</title>
<link rel="stylesheet" href="https://fonts.googleapis.com/css2?family=Bebas+Neue&family=Oswald:wght@500;600&display=swap">
<style>
  :root {
    --cover-brown: #2f1b17;
    --cover-brown-deep: #24140f;
    --title-white: #ffffff;
    --title-silver: #d9d9d9;
    --accent-gold: #f0be5a;
    --band-ink: #2f1b17;
    --photo-warm: #8a6650;
    --photo-cool: #6f6862;
  }
  * { margin: 0; padding: 0; box-sizing: border-box; }
  html, body {
    width: 800px;
    height: 1200px;
    overflow: hidden;
    background: var(--cover-brown);
  }
  .cover {
    position: relative;
    width: 800px;
    height: 1200px;
    overflow: hidden;
    background: radial-gradient(ellipse at 50% 35%, var(--cover-brown) 0%, var(--cover-brown-deep) 100%);
  }
  .cover-photo {
    position: absolute;
    left: 280px;
    top: 20px;
    width: 280px;
    height: 440px;
    border-radius: 120px 120px 10px 10px;
    background: linear-gradient(180deg, var(--photo-warm) 0%, #b79a88 35%, var(--photo-cool) 70%, #cfcac6 100%);
    opacity: 0.85;
  }
  .title-art {
    position: absolute;
    left: 0;
    top: 0;
    width: 800px;
    height: 1200px;
  }
  .title-word {
    font-family: "Bebas Neue", "Oswald", sans-serif;
    fill: url(#titleSheen);
  }
  .title-word--accent { fill: var(--accent-gold); }
  .title-rule { stroke: var(--accent-gold); stroke-width: 2; }
  .subtitle-band {
    position: absolute;
    left: 0;
    top: 1052px;
    width: 800px;
    height: 54px;
    background: var(--accent-gold);
    display: flex;
    align-items: center;
    justify-content: center;
  }
  .subtitle {
    font-family: "Oswald", sans-serif;
    font-weight: 600;
    font-size: 29px;
    letter-spacing: 0.2px;
    color: var(--band-ink);
    text-transform: uppercase;
    transform: scaleX(0.78);
    white-space: nowrap;
  }
  .author {
    position: absolute;
    left: 0;
    top: 1130px;
    width: 800px;
    text-align: center;
    font-family: "Oswald", sans-serif;
    font-weight: 500;
    font-size: 30px;
    letter-spacing: 14px;
    color: var(--title-white);
    text-transform: uppercase;
  }
</style>
</head>
<body>
  <main class="cover">
    <div class="cover-photo" role="img" aria-label="Photograph of a young boy sitting hunched over with his hands holding his head"></div>

    <svg class="title-art" viewBox="0 0 800 1200" aria-labelledby="bookTitle">
      <title id="bookTitle">Quieter Under Lanterns</title>
      <defs>
        <linearGradient id="titleSheen" x1="0" y1="0" x2="1" y2="0">
          <stop offset="0" stop-color="var(--title-white)"/>
          <stop offset="0.3" stop-color="var(--title-silver)"/>
          <stop offset="0.55" stop-color="var(--title-white)"/>
          <stop offset="0.8" stop-color="var(--title-silver)"/>
          <stop offset="1" stop-color="var(--title-white)"/>
        </linearGradient>
      </defs>
      <text class="title-word" x="45" y="650" font-size="278" textLength="710" lengthAdjust="spacingAndGlyphs">QUIETER</text>
      <line class="title-rule" x1="48" y1="727" x2="245" y2="727"/>
      <line class="title-rule" x1="563" y1="727" x2="760" y2="727"/>
      <text class="title-word title-word--accent" x="257" y="795" font-size="193" textLength="288" lengthAdjust="spacingAndGlyphs">UNDER</text>
      <text class="title-word" x="48" y="1030" font-size="320" textLength="727" lengthAdjust="spacingAndGlyphs">LANTERNS</text>
    </svg>

    <div class="subtitle-band">
      <p class="subtitle">A Ledger of Harbour Songs Across Mild Winters</p>
    </div>

    <p class="author">Author Name</p>
  </main>
</body>
</html>
```